Recreate-branding of doctor office forms

There are forms that need to be re created in vector format following the branding guidelines that are provided. This is a typesetting job not a overly creative job. We are looking for a rebuild on existing forms and have attention to detail.
Updates

Hi All - We would need vector files to be provided in either an EPS format or a PDF. There is a brand identity sheet included with the zip file which was uploaded. We will consider increasing our bid, however, please take the time to look it over. This is a very simple, typeset job and low on the creative. Thanks for your time. TK

Industry/Entity Type

Doctor

```html
<!DOCTYPE html>
<html lang="en">
<head>
<meta charset="utf-8">
<title>Insurance Subscriber Information – Meridian Oral &amp; Facial Surgery</title>
<link href="https://fonts.googleapis.com/css2?family=Jost:wght@300&display=swap" rel="stylesheet">
<style>
  :root {
    --ink: #1a1a1a;
    --rule: #3a3a3a;
    --page-edge: #8a8a8a;
    --shade: #e6e6e6;
    --paper: #ffffff;
  }
  html, body {
    margin: 0;
    padding: 0;
    overflow: hidden;
    background: var(--paper);
  }
  .page {
    position: relative;
    width: 927px;
    height: 1200px;
    box-sizing: border-box;
    border: 1px solid var(--page-edge);
    background: var(--paper);
    font-family: "Jost", "Helvetica Neue", Arial, sans-serif;
    font-weight: 300;
    color: var(--ink);
    overflow: hidden;
  }
  .brand {
    position: absolute;
    top: 38px;
    right: 36px;
    display: flex;
    align-items: center;
    gap: 10px;
    color: var(--ink);
  }
  .brand-mark {
    width: 40px;
    height: 40px;
    border-radius: 50%;
    background: var(--ink);
  }
  .brand-text {
    display: flex;
    flex-direction: column;
    line-height: 1;
  }
  .brand-name {
    font-size: 44px;
    letter-spacing: 0.5px;
  }
  .brand-tagline {
    font-size: 10.5px;
    letter-spacing: 1.4px;
    margin-top: 3px;
    text-align: right;
  }
  .subscriber-block {
    position: absolute;
    left: 36px;
    width: 857px;
    height: 256px;
    box-sizing: border-box;
    border: 1px solid var(--rule);
    display: grid;
    grid-template-columns: 265px 1fr;
    grid-template-rows: repeat(9, 1fr);
  }
  .field-label,
  .field-value {
    border-bottom: 1px solid var(--rule);
    box-sizing: border-box;
  }
  .field-label {
    border-right: 1px solid var(--rule);
    padding-left: 22px;
    font-size: 16.5px;
    display: flex;
    align-items: center;
  }
  .field-label.is-shaded { background: var(--shade); }
  .field-label:nth-last-child(2),
  .field-value:last-child { border-bottom: none; }
  .block-1 { top: 117px; }
  .block-2 { top: 381px; }
  .block-3 { top: 646px; }
  .block-4 { top: 910px; }
</style>
</head>
<body>
<main class="page">
  <header class="brand">
    <span class="brand-mark"></span>
    <span class="brand-text">
      <span class="brand-name">Meridian</span>
      <span class="brand-tagline">Oral &amp; Facial Surgery</span>
    </span>
  </header>

  <section class="subscriber-block block-1">
    <div class="field-label">Subscriber Name:</div><div class="field-value"></div>
    <div class="field-label is-shaded">Subscriber DOB:</div><div class="field-value"></div>
    <div class="field-label">Subscriber ID #:</div><div class="field-value"></div>
    <div class="field-label is-shaded">Subscriber Employer:</div><div class="field-value"></div>
    <div class="field-label">Subscriber SSN:</div><div class="field-value"></div>
    <div class="field-label is-shaded">Insurance Name:</div><div class="field-value"></div>
    <div class="field-label">Insurance Phone:</div><div class="field-value"></div>
    <div class="field-label is-shaded">Insurance Group#:</div><div class="field-value"></div>
    <div class="field-label">Insurance Coverage Type:</div><div class="field-value"></div>
  </section>

  <section class="subscriber-block block-2">
    <div class="field-label">Subscriber Name:</div><div class="field-value"></div>
    <div class="field-label is-shaded">Subscriber DOB:</div><div class="field-value"></div>
    <div class="field-label">Subscriber ID #:</div><div class="field-value"></div>
    <div class="field-label is-shaded">Subscriber Employer:</div><div class="field-value"></div>
    <div class="field-label">Subscriber SSN:</div><div class="field-value"></div>
    <div class="field-label is-shaded">Insurance Name:</div><div class="field-value"></div>
    <div class="field-label">Insurance Phone:</div><div class="field-value"></div>
    <div class="field-label is-shaded">Insurance Group#:</div><div class="field-value"></div>
    <div class="field-label">Insurance Coverage Type:</div><div class="field-value"></div>
  </section>

  <section class="subscriber-block block-3">
    <div class="field-label">Subscriber Name:</div><div class="field-value"></div>
    <div class="field-label is-shaded">Subscriber DOB:</div><div class="field-value"></div>
    <div class="field-label">Subscriber ID #:</div><div class="field-value"></div>
    <div class="field-label is-shaded">Subscriber Employer:</div><div class="field-value"></div>
    <div class="field-label">Subscriber SSN:</div><div class="field-value"></div>
    <div class="field-label is-shaded">Insurance Name:</div><div class="field-value"></div>
    <div class="field-label">Insurance Phone:</div><div class="field-value"></div>
    <div class="field-label is-shaded">Insurance Group#:</div><div class="field-value"></div>
    <div class="field-label">Insurance Coverage Type:</div><div class="field-value"></div>
  </section>

  <section class="subscriber-block block-4">
    <div class="field-label">Subscriber Name:</div><div class="field-value"></div>
    <div class="field-label is-shaded">Subscriber DOB:</div><div class="field-value"></div>
    <div class="field-label">Subscriber ID #:</div><div class="field-value"></div>
    <div class="field-label is-shaded">Subscriber Employer:</div><div class="field-value"></div>
    <div class="field-label">Subscriber SSN:</div><div class="field-value"></div>
    <div class="field-label is-shaded">Insurance Name:</div><div class="field-value"></div>
    <div class="field-label">Insurance Phone:</div><div class="field-value"></div>
    <div class="field-label is-shaded">Insurance Group#:</div><div class="field-value"></div>
    <div class="field-label">Insurance Coverage Type:</div><div class="field-value"></div>
  </section>
</main>
</body>
</html>
```